Flyer für Immobilienmakler
Zielgruppe
Wir, die Wendtal Immobilien GmbH, vermitteln Häuser, Wohnungen und Grundstücke, unsere Zielgruppe sind Verkäufer und Kaufinteressenten aus der Region, Immobilien zur Vermittlung gesucht
Aufgabenstellung
Unverbindliche Ersteinschätzung, Ansprechpartner vor Ort, regionale Marktkenntnis. Max. Din A 5, Immobilien zur Vermittlung gesucht.
- Flyer nur zur Immobilienvermittlung

```html
<!DOCTYPE html>
<html lang="de">
<head>
<meta charset="utf-8">
<title>Wendtal Immobilien – Immobilien gesucht</title>
<link href="https://fonts.googleapis.com/css2?family=Poppins:wght@200;300;400;500;600;700&display=swap" rel="stylesheet">
<style>
  :root{
    --gold:#bda068;
    --gold-band:#c0a56c;
    --slate:#45434f;
    --slate-glass:rgba(58,56,70,0.86);
    --ink:#2f2f35;
    --white:#ffffff;
  }
  *{margin:0;padding:0;box-sizing:border-box}
  html,body{width:868px;height:1200px;overflow:hidden;background:#fff}
  body{font-family:"Poppins",sans-serif;color:var(--ink)}
  .flyer{position:relative;width:868px;height:1200px;overflow:hidden;background:var(--white)}

  .brand{position:absolute;left:60px;top:62px;display:flex;align-items:center;gap:12px}
  .brand-mark{width:16px;height:16px;background:var(--slate)}
  .brand-name{font-size:21px;font-weight:500;color:var(--slate);letter-spacing:.2px}

  .slogan{position:absolute;left:380px;top:60px;width:418px;font-size:19.5px;font-weight:600;color:var(--gold);letter-spacing:.6px;padding-bottom:10px;border-bottom:2px solid var(--ink)}

  .hero-photo{position:absolute;left:0;top:142px;width:868px;height:471px;
    background:linear-gradient(180deg,#9cc3e6 0%,#c9dcea 22%,#b98a6c 40%,#8a9a63 58%,#5f8440 78%,#4d6e34 100%)}

  .panel{position:absolute;left:415px;top:438px;width:453px;height:645px;background:var(--slate)}
  .panel-glass{position:absolute;left:415px;top:438px;width:453px;height:175px;background:var(--slate-glass)}
  .panel-notch{position:absolute;left:415px;top:438px}

  .kicker{position:absolute;right:46px;top:492px;font-size:15px;font-weight:700;color:var(--gold);letter-spacing:.4px}
  .headline{position:absolute;right:42px;top:528px;text-align:right;color:var(--white);line-height:1}
  .headline-light{display:block;font-size:61px;font-weight:300;letter-spacing:1.5px}
  .headline-bold{display:block;font-size:74px;font-weight:700;letter-spacing:2px;margin-top:8px}

  .benefits{position:absolute;left:462px;top:702px;list-style:none}
  .benefits li{display:flex;align-items:center;height:32px;margin-bottom:23.5px;font-size:15.5px;font-weight:600;color:var(--white)}
  .tick{width:32px;height:32px;background:var(--gold);margin-right:16px;flex:none}

  .cta{position:absolute;left:454px;top:960px;width:376px;height:66px;background:var(--gold);color:var(--white);font-size:21px;font-weight:600;letter-spacing:1px;display:flex;align-items:center;justify-content:center}

  .intro{position:absolute;left:34px;top:650px;width:370px}
  .intro-title{font-size:24px;font-weight:600;color:var(--gold);line-height:1.32;margin-bottom:22px}
  .intro p{font-size:17.3px;line-height:31px;color:var(--ink);margin-bottom:17px}

  .footer{position:absolute;left:0;top:1082px;width:868px;height:118px;background:var(--gold-band);color:var(--ink);font-size:15.5px;font-weight:500;letter-spacing:2.6px}
  .footer-item{position:absolute;display:flex;align-items:center;gap:14px;white-space:nowrap}
  .footer-item svg{flex:none}
</style>
</head>
<body>
<div class="flyer">

  <div class="brand">
    <span class="brand-mark"></span>
    <span class="brand-name">Wendtal Immobilien GmbH</span>
  </div>

  <div class="slogan">WE MAKE YOUR DREAMS COME TRUE</div>

  <div class="hero-photo" role="img" aria-label="Foto eines Landhauses mit Ziegeldach und Solaranlage, gepflegtem Garten und Naturpool unter blauem Himmel"></div>

  <div class="panel"></div>
  <div class="panel-glass"></div>
  <svg class="panel-notch" width="72" height="70" viewBox="0 0 72 70"><polygon points="0,0 72,0 0,70" fill="#bda068"/></svg>

  <div class="kicker">VERKAUF, RUHIG &amp; PROFESSIONELL</div>
  <h1 class="headline">
    <span class="headline-light">IMMOBILIEN</span>
    <span class="headline-bold">GESUCHT</span>
  </h1>

  <ul class="benefits">
    <li><svg class="tick" viewBox="0 0 32 32"><rect width="32" height="32" fill="#bda068"/><polyline points="9,16.5 14,21 23,11" fill="none" stroke="#fff" stroke-width="2.4"/></svg>Persönliche &amp; ehrliche Wertermittlung</li>
    <li><svg class="tick" viewBox="0 0 32 32"><rect width="32" height="32" fill="#bda068"/><polyline points="9,16.5 14,21 23,11" fill="none" stroke="#fff" stroke-width="2.4"/></svg>Regionale Marktkenntnis</li>
    <li><svg class="tick" viewBox="0 0 32 32"><rect width="32" height="32" fill="#bda068"/><polyline points="9,16.5 14,21 23,11" fill="none" stroke="#fff" stroke-width="2.4"/></svg>Diskrete Abwicklung</li>
    <li><svg class="tick" viewBox="0 0 32 32"><rect width="32" height="32" fill="#bda068"/><polyline points="9,16.5 14,21 23,11" fill="none" stroke="#fff" stroke-width="2.4"/></svg>Keine Verpflichtung durch Ihre Anfrage</li>
  </ul>

  <div class="cta">JETZT BERATEN LASSEN</div>

  <section class="intro">
    <h2 class="intro-title">Sie überlegen, Ihre Immobilie zu verkaufen ?</h2>
    <p>Wir suchen Häuser, Wohnungen und Grundstücke zur Vermittlung, teilweise bereits für vorgemerkte, geprüfte Kaufinteressenten aus der Region.</p>
    <p>Als regional tätiges Immobilienunternehmen begleiten wir Eigentümer sachlich, transparent und ohne Verkaufsdruck – von der ersten Einschätzung bis zum Abschluss.</p>
  </section>

  <footer class="footer">
    <div class="footer-item" style="left:105px;top:24px">Wendtal Immobilien GmbH</div>
    <div class="footer-item" style="left:468px;top:20px">
      <svg width="18" height="26" viewBox="0 0 18 26"><path d="M9 0C4 0 0 4 0 9c0 7 9 17 9 17s9-10 9-17c0-5-4-9-9-9z" fill="#2f2f35"/><circle cx="9" cy="9" r="3.5" fill="#c0a56c"/></svg>
      Mühlweg 7, 84390 Wendtal
    </div>
    <div class="footer-item" style="left:60px;top:66px">
      <svg width="26" height="18" viewBox="0 0 26 18"><rect x="1" y="1" width="24" height="16" fill="none" stroke="#2f2f35" stroke-width="2"/><polyline points="1,1 13,10 25,1" fill="none" stroke="#2f2f35" stroke-width="2"/></svg>
      kontakt@wendtal-immo.de
    </div>
    <div class="footer-item" style="left:522px;top:64px">
      <svg width="24" height="24" viewBox="0 0 24 24"><path d="M6.6 10.8c1.4 2.8 3.8 5.1 6.6 6.6l2.2-2.2c.3-.3.7-.4 1-.2 1.1.4 2.3.6 3.6.6.6 0 1 .4 1 1V20c0 .6-.4 1-1 1C10.6 21 3 13.4 3 4c0-.6.4-1 1-1h3.5c.6 0 1 .4 1 1 0 1.3.2 2.5.6 3.6.1.3 0 .7-.2 1z" fill="#2f2f35"/></svg>
      +49 85 00 413270-0
    </div>
  </footer>

</div>
</body>
</html>
```